military training website telvoquarry.com

I have a website that someone designed I am not happy with. It looks like the designer did not have the artistic ability to make a quality product. the power points are ideas that I had for the website. the business proposal was designed by someone else, and I like the style and font used, the website should reflect this document. The main part of the website should be informational with few pictures, maybe some background images behind or off to the side of the text. I would like to include a generic map with four locations marked, which, when you hover the cursor over them, show a picture of the actual location with an artistic effect or blurred so it doesn't look like a pelquin charts snip, and a picture that resembles what services are offered there, along with the text description, pictures can be found in the documents I attached, also can be stock images. this is outlined in the power points roughly.
Want to have the side menu of the major topics, or at the top, and scroll down a single page to find all of the information we have to offer

Target Market(s)

Special operations military

Industry/Entity Type

military

Coding

Coded - Design and coding required

Number of Pages Required

1 page

Font styles to use
Other font styles liked:
• Agency FB

Colors
0054AA
0677BA
7BADD7
CADEEF
E8F1F8
00AB8E
00BBA5
67D7C9
C6EFE9
E9F9F6

Requirements
Must have
• interactive "map"
Nice to have
• professional design features to make it look like a professional website, not a beginner designer

```html
<!DOCTYPE html>
<html lang="en">
<head>
<meta charset="utf-8">
<title>Telvo Quarry – Master The Mission</title>
<link href="https://fonts.googleapis.com/css2?family=Urbanist:wght@400;500;600;700;800&display=swap" rel="stylesheet">
<style>
:root{
  --navy:#0a1a4a;
  --blue:#0054AA;
  --blue-mid:#0677BA;
  --blue-light:#7BADD7;
  --blue-pale:#CADEEF;
  --blue-mist:#E8F1F8;
  --teal:#00AB8E;
  --teal-bright:#00BBA5;
  --teal-light:#67D7C9;
  --teal-pale:#C6EFE9;
  --white:#ffffff;
  --ink:#333;
  --muted:#666;
  --line:#d6d6d6;
}
*{box-sizing:border-box;margin:0;padding:0}
html,body{width:1200px;height:4800px;overflow:hidden}
body{position:relative;font-family:"Urbanist",sans-serif;color:var(--ink);background:var(--white)}
.abs{position:absolute}

/* hero */
.hero{left:0;top:0;width:1200px;height:720px;background:linear-gradient(160deg,#0b1b4f 0%,#2a3f7e 45%,#5c6f9e 70%,#263a78 100%)}
.brand{left:145px;top:40px;display:flex;align-items:center;gap:12px;color:var(--white);font-weight:700;font-size:22px;letter-spacing:1px}
.brand-dot{width:18px;height:18px;border-radius:50%;background:var(--teal-bright)}
.nav{left:455px;top:38px;display:flex;gap:32px;color:var(--white);font-size:14px;font-weight:500;align-items:center}
.nav .sep{width:1px;height:32px;background:rgba(255,255,255,.6)}
.hero-title{left:0;width:1200px;top:262px;text-align:center;color:var(--white)}
.hero-title h1{font-size:50px;font-weight:700;letter-spacing:1px}
.hero-title p{font-size:27px;font-weight:500;margin-top:2px}
.round-btn{width:38px;height:38px;border-radius:50%;background:var(--white);display:flex;align-items:center;justify-content:center}
.mission{left:205px;top:512px;width:790px;height:180px;background:var(--teal);border-radius:70px 0 70px 0;text-align:center;color:var(--white);padding:42px 60px 0}
.mission h2{font-size:32px;font-weight:600;letter-spacing:1px}
.mission p{font-size:15px;line-height:24px;margin-top:14px}

/* provide */
.provide{left:0;top:600px;width:1200px;height:912px}
.provide-title{left:145px;top:848px;color:var(--white);font-size:46px;font-weight:700;line-height:46px}
.provide-text{left:388px;top:850px;width:668px;color:var(--white);font-size:14.6px;line-height:24px;text-align:justify}
.service{top:1027px;width:200px;color:var(--white)}
.service .icon{width:166px;height:166px;border-radius:50%;background:var(--teal);display:flex;align-items:center;justify-content:center;margin-left:1px}
.service h3{font-size:20px;font-weight:600;line-height:24px;margin-top:20px;min-height:48px}
.service p{font-size:11.3px;line-height:16px;text-align:justify;margin-top:12px}
.divider{top:1045px;width:1px;height:360px;background:rgba(255,255,255,.35)}
.chev{color:var(--white);font-size:30px}

/* map */
.intro{left:200px;top:1603px;width:800px;text-align:center;font-size:14.6px;line-height:24px;color:var(--muted)}
.site-map{left:140px;top:1757px;width:918px;height:524px;background:radial-gradient(ellipse at 50% 50%,#c9a879 0%,#a6855a 45%,#8a7560 75%,#7d7669 100%)}
.marker{width:26px;height:26px;border-radius:50%;border:2px solid var(--white);background:rgba(255,255,255,.25);color:var(--white);font-size:18px;line-height:21px;text-align:center}
.tip{left:445px;top:1767px;width:132px;height:132px;background:var(--blue-mid);color:var(--white);font-size:12px;font-weight:600;line-height:20px;padding:10px 14px;border-radius:2px}

/* qualifications */
.quals{left:0;top:2390px;width:1200px;height:620px;background:linear-gradient(100deg,var(--teal) 0%,var(--teal-bright) 35%,#5fa3cf 60%,#9cc6e6 80%,#d8e8f4 100%)}
.quals-title{left:143px;top:2495px;color:var(--white);font-size:48px;font-weight:600;line-height:48px}
.quals-text{left:143px;top:2606px;width:434px;color:var(--white);font-size:15px;line-height:24px;text-align:justify}

/* contact */
.contact-title{left:0;width:1200px;top:3060px;text-align:center;font-size:50px;font-weight:600;color:#333}
.field{width:323px;height:50px;border:1px solid var(--line);background:var(--white);font-size:11.5px;color:#777;padding:17px 16px}
.submit{left:610px;top:3369px;width:322px;height:50px;background:var(--teal);color:var(--white);font-size:12px;font-weight:700;text-align:center;line-height:50px}

/* gallery */
.gallery-title{left:0;width:1200px;top:3670px;text-align:center;font-size:48px;font-weight:600;color:#333}
.photo{width:287px}
.dark-btn{width:38px;height:38px;border-radius:50%;background:var(--blue);display:flex;align-items:center;justify-content:center}

/* footer */
.foot-brand{left:210px;top:4520px;display:flex;align-items:center;gap:12px;color:var(--white);font-weight:700;font-size:26px}
.foot-head{color:var(--teal-light);font-size:24px;font-weight:600;letter-spacing:.5px}
.foot-links{left:512px;top:4510px;color:var(--white);font-size:13px;line-height:24px}
.foot-div{top:4460px;width:1px;height:190px;background:rgba(255,255,255,.35)}
.info{display:flex;gap:16px;color:var(--white);font-size:13px;line-height:24px}
.info-icon{width:26px;height:26px;border-radius:50%;background:var(--teal);flex:none;display:flex;align-items:center;justify-content:center}
.copy{left:0;width:1200px;top:4724px;text-align:center;color:var(--white);font-size:12.5px}
</style>
</head>
<body>

<!-- hero -->
<div class="abs hero" role="img" aria-label="Night airfield photo with tiltrotor aircraft and special operations vehicle, blue tinted"></div>
<div class="abs brand"><span class="brand-dot"></span>TELVO QUARRY</div>
<nav class="abs nav"><span>Mission</span><span>What We Provide</span><span>Map</span><span>Qualifications</span><span>Contact</span><span>Gallery</span><span class="sep"></span>
<svg width="14" height="14" viewBox="0 0 14 14"><circle cx="6" cy="6" r="4.5" fill="none" stroke="#fff" stroke-width="2"/><line x1="9.5" y1="9.5" x2="13" y2="13" stroke="#fff" stroke-width="2"/></svg></nav>
<div class="abs hero-title"><h1>TELVO QUARRY</h1><p>Master The Mission</p></div>
<div class="abs round-btn" style="left:143px;top:312px"><svg width="10" height="12"><polyline points="7,1 2,6 7,11" fill="none" stroke="#333" stroke-width="1.6"/></svg></div>
<div class="abs round-btn" style="left:1018px;top:312px"><svg width="10" height="12"><polyline points="3,1 8,6 3,11" fill="none" stroke="#333" stroke-width="1.6"/></svg></div>

<!-- blue band -->
<svg class="abs" style="left:0;top:590px" width="1200" height="922" viewBox="0 0 1200 922">
  <defs><linearGradient id="blueBand" x1="0" y1="0" x2="0" y2="1"><stop offset="0" stop-color="#1e63c4"/><stop offset="1" stop-color="#0b4fb0"/></linearGradient></defs>
  <polygon points="0,110 1200,10 1200,922 0,922" fill="url(#blueBand)" role="img" aria-label="Blue camouflage pattern background"/>
  <polygon points="0,104 1200,4 1200,14 0,114" fill="var(--teal-light)"/>
</svg>
<div class="abs mission"><h2>MISSION</h2><p>Pioneering realistic training within a strategic theater across the full spectrum of SOF capabilities, liberating warriors from the shackles of logistical burdens and unleashing their full potential to vanquish adversaries</p></div>

<div class="abs provide-title">WHAT<br>WE<br>PROVIDE</div>
<p class="abs provide-text">At Telvo Quarry, we draw upon years of invaluable experience gained from training at SOF facilities worldwide. Our journey has culminated in the creation of an all-encompassing training site tailored to meet the exacting needs of SOF operators. We provide a comprehensive range of training modalities meticulously crafted to enhance SOF tactics. Anchored by an unwavering commitment to realism and operational effectiveness, we ensure that your warriors are fully prepared to conquer the most demanding challenges they may face.</p>

<div class="abs chev" style="left:60px;top:1203px">‹</div>
<div class="abs chev" style="left:1118px;top:1203px">›</div>

<div class="abs service" style="left:145px"><div class="icon"><svg width="80" height="80" viewBox="0 0 80 80"><path d="M10 62 L22 50 L18 46 L48 18 L54 12 L60 16 L56 22 L62 28 L52 36 L44 34 L34 44 L38 48 L30 58 L26 54 L16 66 Z" fill="#fff"/></svg></div><h3>Precision Marksmanship</h3><p>Utilizing Tier 1 level instructors alongside seasoned local tactical shooting experts, our comprehensive programs incorporate practice with both steel and paper targets, conducted across multiple shooting locations for varied training environments.</p></div>
<div class="abs divider" style="left:358px"></div>
<div class="abs service" style="left:384px"><div class="icon"><svg width="80" height="80" viewBox="0 0 80 80"><polygon points="40,8 68,24 68,56 40,72 12,56 12,24" fill="none" stroke="#fff" stroke-width="6"/><polygon points="40,24 54,32 54,48 40,56 26,48 26,32" fill="#fff"/></svg></div><h3>Immersive Scenarios</h3><p>We have transformed a former Soviet military stronghold into a dynamic training environment, meticulously furnished with explosives, pyrotechnics, and a live Opposition Force for versimilar assault scenarios. Underground lays an intricate tunnel system ideal for confined-space rescue and medical training.</p></div>
<div class="abs divider" style="left:597px"></div>
<div class="abs service" style="left:623px"><div class="icon"><svg width="84" height="80" viewBox="0 0 84 80"><rect x="52" y="10" width="16" height="8" fill="#fff"/><rect x="57" y="18" width="6" height="34" fill="#fff"/><path d="M8 30 L30 30 L36 22 L42 22 L38 32 L48 32 L48 38 L38 38 L42 48 L36 48 L30 40 L8 40 Z" fill="#fff"/><rect x="8" y="56" width="68" height="6" fill="#fff"/><rect x="12" y="66" width="60" height="4" fill="#fff"/></svg></div><h3>Airfield Dominance</h3><p>With a sprawling 7000ft runway available, we provide an expansive canvas for a myriad of airfield operations, including seizures, static line operations, military free fall, and helicopter insertion and extraction techniques.</p></div>
<div class="abs divider" style="left:837px"></div>
<div class="abs service" style="left:862px"><div class="icon"><svg width="80" height="80" viewBox="0 0 80 80"><circle cx="40" cy="16" r="8" fill="#fff"/><circle cx="20" cy="38" r="7" fill="#fff"/><circle cx="60" cy="38" r="7" fill="#fff"/><rect x="10" y="48" width="20" height="22" rx="4" fill="#fff"/><rect x="50" y="48" width="20" height="22" rx="4" fill="#fff"/><path d="M30 52 L40 30 L50 52" fill="none" stroke="#fff" stroke-width="5"/></svg></div><h3>JTAC Support</h3><p>Our team comprises skilled JTACs ready to replicate aircraft in Close Air Support simulations, guaranteeing operators engage in authentic training for air-to-ground coordination, sharpening the skills needed to execute precision strikes with unmatched effectiveness.</p></div>

<!-- map -->
<p class="abs intro">At Telvo Quarry OÜ, our paramount mission is to extend our hospitality to your esteemed team, immersing you in dynamic and authentic training scenarios that cover every aspect of your SOF prowess. We take charge of the logistical challenges, allowing your team to fully concentrate on mastering the mission in Eastern Europe. Our steadfast dedication ensures that every SOF warrior attains the pinnacle of performance and resolute readiness, empowering you to excel in your noble mission: the relentless pursuit of absolute victory with decisive force!</p>
<div class="abs site-map" role="img" aria-label="Illustrated overhead map of the training site with village, roads and ranges"></div>
<div class="abs marker" style="left:498px;top:1932px">+</div>
<div class="abs marker" style="left:716px;top:1872px">+</div>
<div class="abs marker" style="left:441px;top:2072px">+</div>
<div class="abs marker" style="left:786px;top:2072px">+</div>
<div class="abs tip">Site 1<br>Village Complex<br>Tunnel System<br>MFF<br>HLZ<br>Opfor Lodging</div>
<svg class="abs" style="left:500px;top:1898px" width="20" height="12"><polygon points="0,0 20,0 10,12" fill="var(--blue-mid)"/></svg>

<!-- qualifications -->
<div class="abs quals" role="img" aria-label="Tiltrotor aircraft in blue sky with parachutist, over teal camouflage"></div>
<svg class="abs" style="left:0;top:2900px" width="1200" height="130" viewBox="0 0 1200 130">
  <polygon points="0,110 1200,0 1200,130 0,130" fill="#fff"/>
  <polygon points="0,100 1200,-8 1200,6 0,116" fill="var(--blue)"/>
</svg>
<div class="abs quals-title">QUALIFICATIONS<br>SUMMARY</div>
<p class="abs quals-text">The founders of Telvo Quarry OÜ bring forth a wealth of experience and expertise to the table. A former USAF Combat Controller, with nearly a decade of service in Europe; and a highly esteemed former Estonian Special Operator who graduated BUDs and Ranger School, with a proven track record of business success in Estonia. Together, we are steadfast in our dedication to delivering world-class training experiences, deeply rooted in operational excellence and strategic foresight.</p>

<!-- contact -->
<div class="abs contact-title">CONTACT US</div>
<div class="abs field" style="left:265px;top:3153px">First name</div>
<div class="abs field" style="left:265px;top:3225px">Last name</div>
<div class="abs field" style="left:265px;top:3297px">Email</div>
<div class="abs field" style="left:265px;top:3369px">Phone</div>
<div class="abs field" style="left:610px;top:3153px;width:322px;height:195px">Text here...</div>
<div class="abs submit">SUBMIT NOW</div>

<!-- gallery -->
<svg class="abs" style="left:0;top:3525px" width="1200" height="875" viewBox="0 0 1200 875">
  <defs><linearGradient id="mist" x1="0" y1="0" x2="0" y2="1"><stop offset="0" stop-color="var(--blue-mist)"/><stop offset="1" stop-color="#f4f8fc"/></linearGradient></defs>
  <polygon points="0,80 1200,0 1200,875 0,875" fill="url(#mist)"/>
</svg>
<div class="abs gallery-title">GALLERY</div>
<div class="abs photo" style="left:141px;top:3757px;height:211px;background:linear-gradient(160deg,#5a6a40,#7d8a55)" role="img" aria-label="Soldiers reviewing a tablet in a field"></div>
<div class="abs photo" style="left:141px;top:3990px;height:210px;background:linear-gradient(180deg,#6b6c70,#8a6a44 70%,#3c3a2c)" role="img" aria-label="Soldiers with radio antenna at dusk"></div>
<div class="abs photo" style="left:455px;top:3757px;height:443px;background:linear-gradient(180deg,#7d8a6a,#5d6b55 50%,#4f8a3a)" role="img" aria-label="Helicopter landing on grass with troops"></div>
<div class="abs photo" style="left:769px;top:3757px;height:211px;background:linear-gradient(180deg,#6c8fb4,#8aa6b8 55%,#74845a)" role="img" aria-label="Free fall parachutist above fields"></div>
<div class="abs photo" style="left:769px;top:3990px;height:210px;background:linear-gradient(180deg,#b8c2c8,#5d6a5a 60%,#3f3f3c)" role="img" aria-label="Shooting range with targets"></div>
<div class="abs" style="left:579px;top:3958px;width:38px;height:38px;border-radius:50%;background:#fff;text-align:center;line-height:36px;font-size:22px;color:#333">+</div>
<div class="abs dark-btn" style="left:64px;top:3959px"><svg width="10" height="12"><polyline points="7,1 2,6 7,11" fill="none" stroke="#fff" stroke-width="1.8"/></svg></div>
<div class="abs dark-btn" style="left:1106px;top:3959px"><svg width="10" height="12"><polyline points="3,1 8,6 3,11" fill="none" stroke="#fff" stroke-width="1.8"/></svg></div>

<!-- footer -->
<svg class="abs" style="left:0;top:4350px" width="1200" height="450" viewBox="0 0 1200 450">
  <polygon points="0,60 1200,0 1200,450 0,450" fill="var(--blue)" role="img" aria-label="Blue camouflage pattern background"/>
  <polygon points="0,50 1200,-8 1200,6 0,64" fill="var(--teal)"/>
</svg>
<div class="abs foot-brand"><span class="brand-dot"></span>TELVO QUARRY</div>
<div class="abs foot-div" style="left:432px"></div>
<div class="abs foot-head" style="left:512px;top:4460px">QUICK LINKS</div>
<div class="abs foot-links">Mission<br>What We Provide<br>Map<br>Qualifications<br>Contact<br>Gallery</div>
<div class="abs foot-div" style="left:724px"></div>
<div class="abs foot-head" style="left:783px;top:4460px">CONTACT INFO</div>
<div class="abs info" style="left:783px;top:4512px"><span class="info-icon"><svg width="10" height="14"><path d="M5 1 a4 4 0 0 1 4 4 c0 3 -4 8 -4 8 s-4 -5 -4 -8 a4 4 0 0 1 4 -4z" fill="#fff"/></svg></span><span>Lorem ipsum dolor sit amet,<br>consectetur</span></div>
<div class="abs info" style="left:783px;top:4584px"><span class="info-icon"><svg width="12" height="12" viewBox="0 0 12 12"><path d="M2 1 L4.5 1 L5.5 4 L4 5 C5 7 6 8 7.5 8.5 L8.5 7 L11 8 L11 10.5 C6 11 1 6 2 1Z" fill="#fff"/></svg></span><span>+1 888 888 8888</span></div>
<div class="abs info" style="left:783px;top:4633px"><span class="info-icon"><svg width="12" height="10"><rect x="0.5" y="0.5" width="11" height="9" fill="#fff"/><polyline points="1,1 6,5 11,1" fill="none" stroke="var(--teal)" stroke-width="1.2"/></svg></span><span>info@companyname.com</span></div>
<div class="abs copy">© Copyrights 2024 Company name | All Rights Reserved</div>

</body>
</html>
```